We are a printed circuit board manufacturer. Need a company professional web site to allow our potential customers to know more about our background, capability and our products. The web site will contain three languages, which are Chinese, English and Japanese. Our audience are mainly electronic companies that procure printed circuit boards. I have a word document that have all the required text in all three languages. The final design should communicate the impression that we embrace quality, trustworthiness and long term partnership business principles.
We should have sections that allow us to post pictures of our facilities.
I have added the three files in three different languages.
Some of the information is below:
Background
RVD Worldwide Limited (RVD) was set up in Hong Kong in 2007 by two Hong Kong entrepreneurs, Mr. Lok Fai Tam and Mr. Wai Ho. We acquired the single sided printed circuit board factory located in Dongguan City, Guangdong Province, China, from Valtor Corporation of the U.S. in 2007. In addition to RVD, Mr. Tam and Mr. Ho also own Brightrail Systems Company Limited, a semiconductor company based in Hong Kong since 1997 with a total investment of over US$100 million. Brightrail is engaged in the manufacturing of flexible substrates and MEMS assembly business.
RVD has been awarded TS 16949 and ISO14000 certificates since 2009 and 2004 respectively.
Business Principles
RVD Worldwide Limited strives to be a professional top notched printed circuit board supplier. We embrace four “EXCELLENCE” principles, namely, excellence in quality, excellence in prices, excellence in services and excellence in on time delivery.
We approach each customer with a long-term partnership view that delivers the lowest ownership costs and highest total values to our customers. We customize quotations and solutions in order to allow our customers to win more businesses. We believe by thinking from our customers’ points of view we will be able to create a WIN-WIN relationship.
Customers
Due to our excellent quality, services and production systems, RVD Worldwide Limited manage to service a number of large Japanese and US customers, which include:
Technical capability overview
Below is an overview of our current capability:
Target Market(s)
Electronic companies buyers
Industry/Entity Type
Business
Requirements
Must have
- Capability description
Should not have
- no cartoon

```html
<!DOCTYPE html>
<html lang="en">
<head>
<meta charset="utf-8">
<title>RVD Worldwide Limited – Printed Circuit Boards</title>
<link rel="stylesheet" href="https://fonts.googleapis.com/css2?family=Arimo:wght@400;700&family=Cinzel:wght@500&family=Encode+Sans+Condensed:wght@500&family=Libre+Caslon+Text&family=Alfa+Slab+One&display=swap">
<style>
  :root{
    --teal:#0d7a66;
    --teal-dark:#07604f;
    --teal-deep:#0b5a4a;
    --orange:#f7931e;
    --orange-light:#fbad3a;
    --text:#555;
    --grey-line:#bbb;
    --panel:#ececec;
    --white:#fff;
  }
  *{margin:0;padding:0;box-sizing:border-box}
  html,body{width:1200px;height:1173px;overflow:hidden;background:var(--white)}
  body{position:relative;font-family:"Arimo",Arial,sans-serif;color:var(--text)}
  .abs{position:absolute}

  .top-strip{left:0;top:0;width:1200px;height:7px;background:var(--teal)}
  .brand{left:110px;top:24px;display:flex;align-items:center;gap:10px;
    font-family:"Cinzel",serif;font-weight:500;font-size:26px;color:var(--teal);line-height:1}
  .brand .mark{width:14px;height:14px;background:var(--teal)}
  .phone{left:966px;top:66px;display:flex;align-items:center;gap:6px;font-size:13px;color:#111}

  .main-nav{left:99px;top:99px;width:1003px;height:36px;background:linear-gradient(#0f8870,var(--teal-dark));
    border-radius:6px 6px 0 0;display:flex;align-items:center}
  .main-nav a{font-family:"Cinzel",serif;font-size:15px;letter-spacing:.5px;color:var(--white);text-decoration:none;position:absolute;top:9px}
  .main-nav .login{right:0;top:0;width:89px;height:36px;background:var(--orange);border-radius:0 6px 0 0;
    font-family:"Arimo",sans-serif;font-weight:700;font-size:14px;display:flex;align-items:center;justify-content:center;gap:6px}

  .hero{left:99px;top:135px;width:1002px;height:303px;border:1px solid #9ab;overflow:hidden;
    background:linear-gradient(90deg,#f4f6f6,#eef1f1 45%,#e2e8ea)}
  .hero-photo{position:absolute;left:410px;top:0;width:592px;height:303px;
    background:linear-gradient(100deg,rgba(238,242,242,0) 0%,#c9d3d8 30%,#3b4e5c 60%,#2b3945 85%,#a9b4ba)}
  .hero h1{position:absolute;left:0;top:17px;width:382px;text-align:center;font-family:"Libre Caslon Text",serif;
    font-weight:400;font-size:27px;line-height:35.5px;color:var(--teal);white-space:nowrap}
  .hero ul{position:absolute;left:34px;top:139px;list-style:none}
  .hero li{font-family:"Encode Sans Condensed",sans-serif;font-weight:500;font-size:20px;color:var(--teal);
    height:32.5px;display:flex;align-items:center;gap:8px}
  .hero-arrow{top:237px}

  .welcome{left:108px;top:476px;width:618px}
  .welcome h2{font-family:"Encode Sans Condensed",sans-serif;font-weight:500;font-size:33px;color:var(--orange);line-height:42px;margin-bottom:4px;white-space:nowrap}
  .welcome p{font-size:13.5px;line-height:24px;text-align:justify;margin-bottom:24px}

  .quick-contact{left:776px;top:475px;width:325px;height:340px}
  .quick-contact .tab{position:absolute;left:39px;top:0;width:244px;height:61px;background:linear-gradient(var(--orange-light),var(--orange));
    border:1px solid #e5b072;font-family:"Alfa Slab One",serif;font-size:22px;letter-spacing:1px;color:var(--white);
    display:flex;align-items:center;justify-content:center}
  .field{position:absolute;left:34px;width:258px;height:35px;background:linear-gradient(#fafafa,#e6e6e6);
    border:1px solid #d6d6d6;font-size:13.5px;letter-spacing:.5px;color:#777;padding:9px 12px}
  .submit{position:absolute;left:214px;top:299px;width:78px;height:29px;background:var(--orange);color:var(--white);
    font-family:"Arimo",sans-serif;font-weight:700;font-size:12px;letter-spacing:1.5px;display:flex;align-items:center;justify-content:center}

  .customers{left:108px;top:853px;width:990px;height:110px;border:1px solid var(--grey-line)}
  .customers h3{position:absolute;left:18px;top:-19px;background:var(--white);padding:0 9px;font-family:"Arimo",sans-serif;
    font-weight:700;font-size:20px;color:var(--orange)}
  .customers .names span{position:absolute;top:40px;font-family:"Arimo",sans-serif;font-weight:700;font-size:23px;color:#1d2b3a;white-space:nowrap}

  .footer{left:0;top:991px;width:1200px;height:145px;background:linear-gradient(#0e7f69,var(--teal-deep))}
  .footer h4{position:absolute;left:108px;top:11px;font-size:12px;font-weight:700;color:var(--white)}
  .links{position:absolute;top:43px;list-style:none}
  .links li{font-size:11px;color:var(--white);line-height:18px}
  .links li::before{content:"➤";font-size:6px;margin-right:5px;vertical-align:2px}
  .address{position:absolute;right:107px;top:14px;text-align:right;font-size:11px;line-height:18px;color:var(--white)}
  .address strong{font-size:12.5px}
  .copyright{left:0;top:1136px;width:1200px;height:37px;background:var(--teal);display:flex;align-items:center;justify-content:center;
    font-size:11px;font-weight:700;color:var(--white)}
</style>
</head>
<body>
  <div class="abs top-strip"></div>

  <header>
    <div class="abs brand"><span class="mark"></span>RVD Worldwide</div>
    <div class="abs phone">
      <svg width="30" height="24" viewBox="0 0 30 24"><ellipse cx="15" cy="13" rx="14" ry="10" fill="#0d7a66"/><path d="M10 9c0 5 4 9 9 9l2-3-3-2-1 1c-2-1-3-2-4-4l1-1-2-3z" fill="#fff"/></svg>
      (852) 2000 4100
    </div>
    <nav class="abs main-nav">
      <a style="left:44px">HOME</a>
      <a style="left:161px">PRODUCTS</a>
      <a style="left:314px">SERVICES</a>
      <a style="left:453px">TECHNICAL CAPABILITIES</a>
      <a style="left:721px">CONTACT US</a>
      <a class="login">
        <svg width="18" height="22" viewBox="0 0 18 22"><path d="M4 10V6a5 5 0 0110 0v4" fill="none" stroke="#ddd" stroke-width="2.5"/><rect x="1" y="10" width="16" height="11" rx="2" fill="#e8e8e8"/></svg>login
      </a>
    </nav>
  </header>

  <svg class="abs hero-arrow" style="left:61px" width="34" height="90" viewBox="0 0 34 90"><path d="M32 0 4 45l28 45" fill="none" stroke="#0d7a66" stroke-width="7"/></svg>
  <svg class="abs hero-arrow" style="left:1104px" width="34" height="90" viewBox="0 0 34 90"><path d="M2 0l28 45L2 90" fill="none" stroke="#0d7a66" stroke-width="7"/></svg>

  <section class="abs hero">
    <div class="hero-photo" role="img" aria-label="Photo of three business professionals in suits gathered around a laptop in a bright office"></div>
    <h1>Our Printed Circuit Board<br>business is committed<br>to "Excellence”</h1>
    <ul>
      <li><svg width="30" height="20" viewBox="0 0 30 20"><path d="M2 11l8 7L28 2" fill="none" stroke="#0d7a66" stroke-width="3.5"/></svg>EXCELLENCE IN QUALITY</li>
      <li><svg width="30" height="20" viewBox="0 0 30 20"><path d="M2 11l8 7L28 2" fill="none" stroke="#0d7a66" stroke-width="3.5"/></svg>EXCELLENCE IN PRICES</li>
      <li><svg width="30" height="20" viewBox="0 0 30 20"><path d="M2 11l8 7L28 2" fill="none" stroke="#0d7a66" stroke-width="3.5"/></svg>EXCELLENCE IN SERVICES</li>
      <li><svg width="30" height="20" viewBox="0 0 30 20"><path d="M2 11l8 7L28 2" fill="none" stroke="#0d7a66" stroke-width="3.5"/></svg>EXCELLENCE IN ON TIME DELIVERY</li>
    </ul>
  </section>

  <section class="abs welcome">
    <h2>WELCOME TO RVD Worldwide Limited (RVD)</h2>
    <p>RVD Worldwide Limited (RVD) was set up in Hong Kong in 2007 by two Hong Kong entrepreneurs, Mr. Lok Fai Tam and Mr. Wai Ho. We acquired the single sided printed circuit board factory located in Dongguan City, Guangdong Province, China, from Valtor Corporation of the U.S. in 2007. In addition to RVD, Mr. Tam and Mr. Ho also own Brightrail Systems Company Limited, a semiconductor company based in Hong Kong since 1997 with a total investment of over US$100 million. Brightrail is engaged in the manufacturing of flexible substrates and the assembly of Micro Electro Mechanical Systems (MEMS).</p>
    <p>RVD has been awarded TS 16949 and ISO14000 certificates since 2009 and 2004 respectively.</p>
  </section>

  <aside class="abs quick-contact">
    <svg style="position:absolute;left:0;top:0" width="325" height="340" viewBox="0 0 325 340">
      <path d="M20 2H305L323 20V320L305 338H20L2 320V20Z" fill="#ececec" stroke="#fff" stroke-width="4"/>
      <path d="M20 2H305L323 20V320L305 338H20L2 320V20Z" fill="none" stroke="#ddd" stroke-width="1" transform="translate(0 1)"/>
    </svg>
    <div class="tab">QUICK CONTACT</div>
    <div class="field" style="top:69px">Name:</div>
    <div class="field" style="top:109px">Email:</div>
    <div class="field" style="top:149px">Company Name:</div>
    <div class="field" style="top:190px;height:101px">Comments:</div>
    <div class="submit">SUBMIT</div>
  </aside>

  <svg class="abs" style="left:82px;top:893px" width="18" height="22" viewBox="0 0 18 22"><path d="M15 2 5 11l10 9" fill="none" stroke="#bbb" stroke-width="4"/></svg>
  <svg class="abs" style="left:1104px;top:893px" width="18" height="22" viewBox="0 0 18 22"><path d="M3 2l10 9-10 9" fill="none" stroke="#bbb" stroke-width="4"/></svg>

  <section class="abs customers">
    <h3>OUR CUSTOMERS</h3>
    <div class="names">
      <span style="left:40px">Norvane</span>
      <span style="left:196px">Halcrest Power</span>
      <span style="left:392px">Brenvoss Energy</span>
      <span style="left:642px">Kestova</span>
      <span style="left:808px">Ordwell</span>
    </div>
  </section>

  <footer class="abs footer">
    <h4>POPULAR LINKS</h4>
    <ul class="links" style="left:108px">
      <li>Sitemap</li><li>Circuit Boardas</li><li>Capabilities</li><li>Industries Served</li><li>About Us</li>
    </ul>
    <ul class="links" style="left:274px">
      <li>Contact Us</li><li>Resources</li><li>Service Center</li><li>News &amp; Events</li><li>Privacy Policy</li>
    </ul>
    <div class="address">
      <strong>RVD Worldwide Limited</strong><br>
      28/F Harbour Crest<br>
      12 Marlow Road<br>
      Wan Chai, HONG KONG<br>
      Telephone: (852)20004100<br>
      Fax: (852)20004199<br>
      Email: sales@rvdboards.example
    </div>
  </footer>
  <div class="abs copyright">COPYRIGHT © 2012 RVD WORLDWIDE LIMITED. ALL RIGHTS RESERVED</div>
</body>
</html>
```